Slick Facebook Ad

We've recently re-branded our business to reflect our ethos "Wealth is about more than money - it's about choice." We aim to protect your hard-earned success and help achieve your lifestyle aspirations, whether that's retiring at fifty to go globetrotting, or buying your first home. We're a financial consultancy that primarily services high-net-worth clients.

Our brand is minimalist, modern (check out our website) and the brief focuses on our strong investment return for the past 12 years.

Task: The attached brief is for a Facebook advertisement. Please see competitor images as a guide to how 'returns' and 'branding' can both be displayed in a design.

Target Market(s)

+30

Font styles to use
Sans Serif

Requirements
Must have
• Creative should feature the strong investment return, and design aesthetic should be 'on-brand' (modern, minimalist, lifestyle focused).

```html
<!DOCTYPE html>
<html lang="en">
<head>
<meta charset="utf-8">
<title>Global Portfolio Returns – Meridian Wealth Partners</title>
<link rel="stylesheet" href="https://fonts.googleapis.com/css2?family=Montserrat:wght@500;600;700&display=swap">
<style>
  :root{
    --bg-light:#ffffff;
    --bg-shade:#e9e9ea;
    --navy:#1f3c82;
    --olive:#8d9c1f;
    --olive-light:#b4c24a;
    --grey:#808080;
    --slate:#7e8490;
    --slate-light:#cdd1d9;
    --footnote:#8c8c8c;
  }
  *{margin:0;padding:0;box-sizing:border-box}
  html,body{width:1200px;height:1200px;overflow:hidden}
  body{font-family:"Montserrat",Arial,sans-serif}
  .ad{
    position:relative;width:1200px;height:1200px;overflow:hidden;
    background:radial-gradient(circle at 20% 15%,var(--bg-light) 0%,#f6f6f6 45%,var(--bg-shade) 100%);
  }
  .version-tag{position:absolute;left:20px;top:14px;font-size:21px;font-weight:600;color:var(--navy)}
  .headline{position:absolute;left:124px;font-weight:600;font-size:51px;letter-spacing:-0.5px;white-space:nowrap}
  .headline--portfolio{
    top:122px;
    background:linear-gradient(90deg,var(--olive) 0%,var(--olive-light) 100%);
    -webkit-background-clip:text;background-clip:text;color:transparent;
  }
  .headline--index{top:598px;color:var(--slate)}
  .figures{position:absolute;inset:0;width:1200px;height:1200px}
  .figures text{font-family:"Montserrat",Arial,sans-serif;font-weight:600}
  .brand{position:absolute;right:62px;top:990px;display:flex;align-items:center;gap:14px}
  .brand__dot{width:34px;height:34px;border-radius:50%;background:var(--olive)}
  .brand__name{font-size:34px;font-weight:600;color:var(--olive)}
  .footnote{position:absolute;right:65px;top:1114px;font-size:21px;font-weight:500;color:var(--footnote);white-space:nowrap}
</style>
</head>
<body>
<main class="ad">
  <p class="version-tag">Version 04</p>

  <h1 class="headline headline--portfolio">Our Global Portfolio returned.</h1>
  <h2 class="headline headline--index">The NXA Returned.</h2>

  <svg class="figures" viewBox="0 0 1200 1200" aria-hidden="false">
    <defs>
      <linearGradient id="portfolioFill" x1="117" y1="0" x2="890" y2="0" gradientUnits="userSpaceOnUse">
        <stop offset="0" stop-color="#a6b52a"/>
        <stop offset="0.45" stop-color="#8f9a4c"/>
        <stop offset="1" stop-color="#808078"/>
      </linearGradient>
      <linearGradient id="indexFill" x1="117" y1="0" x2="660" y2="0" gradientUnits="userSpaceOnUse">
        <stop offset="0" stop-color="#cfd3db"/>
        <stop offset="1" stop-color="#868c98"/>
      </linearGradient>
      <linearGradient id="peakTones" x1="0" y1="230" x2="0" y2="500" gradientUnits="userSpaceOnUse">
        <stop offset="0" stop-color="#e9f0f6"/>
        <stop offset="0.5" stop-color="#9fb6cf"/>
        <stop offset="1" stop-color="#3f6aa4"/>
      </linearGradient>
      <clipPath id="portfolioDigits">
        <text x="117" y="494" font-size="400" textLength="772" lengthAdjust="spacingAndGlyphs">20.3</text>
      </clipPath>
    </defs>

    <text class="figure figure--portfolio" x="117" y="494" font-size="400" textLength="772" lengthAdjust="spacingAndGlyphs" fill="url(#portfolioFill)">20.3</text>
    <g role="img" aria-label="Snowy mountain peaks photograph filling the lower part of the digits" clip-path="url(#portfolioDigits)">
      <polygon points="117,470 200,432 300,418 420,428 560,440 660,400 700,300 725,232 890,232 890,500 117,500" fill="url(#peakTones)"/>
    </g>
    <text class="figure-unit" x="888" y="494" font-size="232" fill="var(--grey)">%</text>

    <polyline class="trend trend--portfolio" fill="none" stroke="var(--navy)" stroke-width="2.6" stroke-linejoin="round"
      points="92,462 105,458 118,460 128,438 136,452 150,447 165,450 180,440 192,445 205,425 218,418 230,430 245,432 258,440 272,428 290,436 305,424 318,428 330,438 345,434 360,444 372,432 385,412 398,422 410,430 425,425 440,436 455,430 470,432 485,430 500,426 512,430 525,418 535,412 548,398 560,390 572,380 585,368 598,352 608,346 618,330 628,318 636,300 645,290 655,270 664,260 672,246 680,228 686,190 690,175 694,190 698,236 705,224 712,300 720,340 728,350 735,320 742,292 750,260 758,240 766,250 774,232 782,236 790,220 797,180 804,196 810,214 818,206 826,250 832,234 840,226 848,248 856,238 864,224 872,212 880,214 888,200 895,188 902,193 908,182 914,196 920,190 926,176"/>

    <text class="figure figure--index" x="117" y="966" font-size="400" textLength="538" lengthAdjust="spacingAndGlyphs" fill="url(#indexFill)">9.5</text>
    <text class="figure-unit" x="664" y="966" font-size="232" fill="#8a909c">%</text>

    <polyline class="trend trend--index" fill="none" stroke="#6d7585" stroke-width="2.2" stroke-linejoin="round"
      points="115,940 125,944 135,936 145,922 155,914 165,920 175,906 190,904 205,896 220,900 232,888 245,892 258,880 270,888 282,874 295,878 308,866 320,870 332,858 345,866 355,856 368,870 380,876 392,888 405,884 418,890 430,884 442,890 455,880 468,870 478,860 490,846 500,836 512,824 522,812 534,804 545,790 556,778 566,786 574,776 584,770 594,754 604,764 612,748 620,740 628,730 636,712 642,706 646,728 650,770 654,752 660,805"/>
  </svg>

  <div class="brand">
    <span class="brand__dot"></span>
    <span class="brand__name">Meridian</span>
  </div>

  <p class="footnote">For 07/12/16 – 07/12/17,&nbsp; Source: Meridian Wealth Partners</p>
</main>
</body>
</html>
```